Trevlo Home Buyers

We need a website designed for the a house buying company. It can look and feel similar to a real estate agency, but the messaging is different. Attached in the document below you will see what we are looking for. The main thing we are going for is clean, corporate and approachable. The Logo files are also attached. We want to use the logo and branding throughout the site.

```html
<!DOCTYPE html>
<html lang="en">
<head>
<meta charset="utf-8">
<title>Trevlo Home Buyers</title>
<link href="https://fonts.googleapis.com/css2?family=Montserrat:wght@500;600;700;800&family=Open+Sans:wght@400;600&display=swap" rel="stylesheet">
<style>
:root{
  --blue:#0d3f8f;
  --blue-dark:#0a3278;
  --green:#5bb12f;
  --gray-bg:#f3f3f3;
  --text:#555;
  --white:#fff;
}
*{box-sizing:border-box;margin:0;padding:0}
html,body{width:1200px;height:5226px;overflow:hidden}
body{font-family:"Open Sans",Arial,sans-serif;color:var(--text);background:var(--white);position:relative}
section,header,footer{position:relative;width:1200px;overflow:hidden}
.hd{font-family:"Montserrat",Arial,sans-serif;font-weight:800;letter-spacing:-.5px}
.blue{color:var(--blue)}.green{color:var(--green)}
.btn{display:inline-flex;align-items:center;justify-content:center;background:var(--green);color:var(--white);font-family:"Montserrat",Arial,sans-serif;font-weight:700;font-size:15px;border-radius:30px}

/* header */
.site-header{height:133px}
.brand{position:absolute;left:110px;top:50px;display:flex;align-items:center;gap:12px;font-family:"Montserrat",Arial,sans-serif;font-weight:700;font-size:24px;color:var(--blue);line-height:1;white-space:nowrap}
.brand .mark{width:22px;height:22px;border-radius:50%;background:var(--blue)}
.call-top{position:absolute;right:110px;top:20px;display:flex;align-items:center;gap:12px;color:var(--green);font-family:"Montserrat",Arial,sans-serif;font-weight:700;font-size:15px}
.icon-circle{width:52px;height:52px;border-radius:50%;background:var(--green);display:flex;align-items:center;justify-content:center}
.main-nav{position:absolute;right:110px;top:94px;display:flex;gap:38px;font-family:"Montserrat",Arial,sans-serif;font-weight:700;font-size:11px;color:#333}
.main-nav .active{color:var(--green)}

/* hero */
.hero{height:737px}
.hero-photo{position:absolute;inset:0;background:linear-gradient(180deg,#8fc0ea 0%,#c7dcef 30%,#c9b79c 55%,#a89a84 72%,#5f9a3a 86%,#4c8a2c 100%)}
.hero-shape{position:absolute;left:0;top:0}
.hero-box{position:absolute;left:293px;top:267px;width:607px;height:227px;background:rgba(20,20,20,.82);text-align:center;padding-top:40px}
.hero-box h1{color:var(--white);font-size:26px}
.hero-box h2{color:var(--green);font-size:24px;margin-top:14px}
.hero-form{position:absolute;left:28px;top:147px;width:560px;height:58px;background:var(--white);border-radius:4px;display:flex;align-items:center;padding:0 6px 0 18px}
.hero-form .ph{flex:1;text-align:left;font-size:12px;color:#555;display:flex;align-items:center;gap:10px}
.hero-form .btn{border-radius:3px;height:44px;width:148px;font-size:13px}

/* thinking */
.thinking{height:663px}
.thinking-photo{position:absolute;left:111px;top:80px;width:395px;height:490px;border:4px solid #e8e8e8;background:linear-gradient(180deg,#5fa5e6 0%,#9fcdf0 35%,#d9b7a0 55%,#c69e86 70%,#4f8f3a 100%)}
.thinking-copy{position:absolute;left:568px;top:80px;width:520px}
.thinking-copy h2{font-size:26px}
.thinking-copy p.lead{font-size:12px;line-height:26px;margin-top:30px}
.reasons{display:flex;gap:50px;margin-top:22px}
.reasons ul{flex:1;list-style:none}
.reasons li{font-size:12px;line-height:26px;padding-left:24px;position:relative;margin-bottom:16px}
.reasons li::before{content:"";position:absolute;left:0;top:7px;width:11px;height:11px;border:1.5px solid var(--green);border-radius:50%}

/* benefits */
.benefits{height:495px;background:var(--gray-bg);text-align:center}
.benefits h2{font-size:28px;padding-top:70px}
.benefits .kicker{font-family:"Montserrat",Arial,sans-serif;font-weight:700;font-size:13px;color:#222;margin-top:14px}
.benefit{position:absolute;top:198px;width:240px;text-align:center}
.benefit .badge{width:122px;height:122px;border-radius:50%;margin:0 auto;display:flex;align-items:center;justify-content:center}
.benefit h3{font-family:"Montserrat",Arial,sans-serif;font-weight:700;font-size:13px;margin-top:24px}
.benefit p{font-size:12px;line-height:24px;margin-top:10px}

/* experts band */
.experts{height:342px;background:linear-gradient(180deg,var(--blue) 0%,var(--blue-dark) 100%);text-align:center}
.experts h2{color:var(--white);font-size:33px;padding-top:108px}
.experts .btn{width:218px;height:56px;margin-top:36px}

/* how */
.how{height:542px}
.how h2{text-align:center;font-size:33px;padding-top:58px}
.step{position:absolute;width:138px;height:138px;margin:-69px 0 0 -69px;border:2px solid var(--green);border-radius:50%;display:flex;align-items:center;justify-content:center;background:var(--white)}
.step-num{position:absolute;width:36px;height:36px;border-radius:50%;color:var(--white);font-family:"Montserrat",Arial,sans-serif;font-weight:700;font-size:16px;display:flex;align-items:center;justify-content:center;left:49px}
.step-label{position:absolute;width:200px;margin-left:-100px;text-align:center;font-family:"Montserrat",Arial,sans-serif;font-weight:600;font-size:14px;color:#222;line-height:26px}
.how-arrows{position:absolute;left:0;top:0}

/* close */
.close-fast{height:641px;background:var(--gray-bg)}
.close-fast h2{text-align:center;font-size:33px;padding-top:58px}
.video{position:absolute;left:196px;top:131px;width:805px;height:450px;background:linear-gradient(180deg,#2f6fc9 0%,#6aa0e0 30%,#b9a188 55%,#8d7c68 72%,#8f8f88 100%);display:flex;align-items:center;justify-content:center}
.play{width:82px;height:82px;border-radius:50%;border:3px solid var(--white);background:rgba(0,0,0,.35);display:flex;align-items:center;justify-content:center}

/* reviews */
.reviews{height:345px;background:var(--green);text-align:center;color:var(--white)}
.reviews h2{font-size:33px;padding-top:44px}
.reviews h3{font-family:"Montserrat",Arial,sans-serif;font-weight:700;font-size:22px;margin-top:8px}
.reviews blockquote{width:720px;margin:34px auto 0;font-size:12px;line-height:27px;position:relative}
.reviews blockquote .q{font-family:Georgia,serif;font-size:30px;font-weight:700;position:absolute}
.reviews .author{font-family:"Montserrat",Arial,sans-serif;font-weight:700;font-size:22px;margin-top:28px}

/* faq */
.faq{height:490px;text-align:center}
.faq h2{font-size:33px;padding-top:46px}
.faq h3{font-family:"Montserrat",Arial,sans-serif;font-weight:700;font-size:22px;margin-top:8px}
.faq-item{position:absolute;top:207px;width:240px;margin-left:-120px;text-align:center}
.faq-item .qc{width:70px;height:70px;border-radius:50%;margin:0 auto;color:var(--white);font-family:"Montserrat",Arial,sans-serif;font-weight:800;font-size:30px;display:flex;align-items:center;justify-content:center}
.faq-item h4{font-family:"Montserrat",Arial,sans-serif;font-weight:600;font-size:12.5px;color:#222;margin-top:18px;line-height:24px}
.faq-item p{font-size:12px;line-height:24px;margin-top:12px}
.faq .btn{position:absolute;left:509px;top:413px;width:182px;height:56px}

/* contact */
.contact{height:485px;background:linear-gradient(180deg,#3a404a 0%,#2a3038 60%,#1f2a20 100%);text-align:center}
.contact h2{color:var(--white);font-size:33px;padding-top:70px}
.contact h3{color:var(--green);font-family:"Montserrat",Arial,sans-serif;font-weight:700;font-size:23px;margin-top:14px}
.field{position:absolute;height:42px;background:var(--white);font-size:12px;color:#333;text-align:left;padding:13px 12px}
.contact .btn{position:absolute;left:513px;top:406px;width:174px;height:52px}

/* footer */
.site-footer{height:353px}
.site-footer .brand{top:94px}
.foot-call{position:absolute;left:368px;top:104px;display:flex;align-items:center;gap:20px}
.foot-call .ring{width:66px;height:66px;border-radius:50%;border:2px solid var(--green);display:flex;align-items:center;justify-content:center}
.foot-call .lbl{font-family:"Montserrat",Arial,sans-serif;font-weight:600;font-size:15px;color:#333}
.foot-call .num{font-family:"Montserrat",Arial,sans-serif;font-weight:700;font-size:18px;color:#333;margin-top:4px}
.social{position:absolute;left:660px;top:68px;text-align:center}
.social h4{font-family:"Montserrat",Arial,sans-serif;font-weight:600;font-size:20px;color:#333}
.social .row{display:flex;gap:9px;margin-top:12px}
.social .row span{width:34px;height:34px;border-radius:50%;border:1.5px solid #999}
.cert{position:absolute;left:877px;top:70px;width:174px;height:68px;border-radius:6px;background:var(--blue)}
.copyright{position:absolute;top:212px;width:100%;text-align:center;font-size:11.5px;color:#333}
.copyright a{color:var(--blue);text-decoration:underline}
.disclaimer{position:absolute;left:111px;top:258px;width:980px;font-size:11.5px;line-height:24px;color:#555}
.disclaimer b{font-family:"Montserrat",Arial,sans-serif;font-size:15px;color:#222;margin-right:10px}
</style>
</head>
<body>

<header class="site-header">
  <div class="brand"><span class="mark"></span>Trevlo Home Buyers</div>
  <div class="call-top">
    <span class="icon-circle"><svg width="22" height="22" viewBox="0 0 24 24"><path d="M6.6 10.8a15 15 0 006.6 6.6l2.2-2.2c.3-.3.7-.4 1-.2 1.1.4 2.3.6 3.6.6.6 0 1 .4 1 1V20c0 .6-.4 1-1 1A17 17 0 013 4c0-.6.4-1 1-1h3.5c.6 0 1 .4 1 1 0 1.3.2 2.5.6 3.6.1.3 0 .7-.2 1z" fill="#fff"/></svg></span>
    CALL US : (555) 010-4477
  </div>
  <nav class="main-nav">
    <span class="active">HOME</span><span>WHY TREVLO HOME BUYERS</span><span>HOW IT WORKS</span><span>REASONS TO SELL</span><span>LOCATIONS</span><span>FAQ</span><span>CONTACT</span>
  </nav>
</header>

<section class="hero">
  <div class="hero-photo" role="img" aria-label="Photo of a two-storey suburban family house with a green lawn under a blue sky"></div>
  <svg class="hero-shape" width="1200" height="737" viewBox="0 0 1200 737">
    <polygon points="0,600 600,722 1200,600 1200,737 0,737" fill="var(--green)"/>
    <polygon points="0,620 600,737 1200,620 1200,737 0,737" fill="#fff"/>
  </svg>
  <div class="hero-box">
    <h1 class="hd">WE BUY HOMES FROM PEOPLE IN A PINCH!</h1>
    <h2 class="hd">GET YOUR CASH OFFER TODAY</h2>
    <div class="hero-form">
      <span class="ph"><svg width="10" height="14" viewBox="0 0 10 14"><path d="M5 0a5 5 0 015 5c0 4-5 9-5 9S0 9 0 5a5 5 0 015-5z" fill="#333"/><circle cx="5" cy="5" r="2" fill="#fff"/></svg>| Enter Your Street Address :</span>
      <span class="btn">Get A Cash Offer</span>
    </div>
  </div>
</section>

<section class="thinking">
  <div class="thinking-photo" role="img" aria-label="Photo of a stucco house with a tiled roof and palm trees"></div>
  <div class="thinking-copy">
    <h2 class="hd"><span class="blue">THINKING</span> <span class="green">OF SELLING?</span></h2>
    <p class="lead">No matter your situation, we will buy your home. No need to worry about the condition of the house either - we'll make this a stress-free process &amp; get you cash quickly.</p>
    <div class="reasons">
      <ul>
        <li>Retirement</li>
        <li>Divorce</li>
        <li>Massive Repairs - Is your home to much to manage? No problem; our team is happy to take it off your hands.</li>
        <li>Probate</li>
        <li>Moving - Sometimes you just want to move and that's okay too! Let us help you get into your dream home.</li>
      </ul>
      <ul>
        <li>Downsizing or Upsizing</li>
        <li>Inheritance - Have you inherited home &amp; you don't want to worry about the head ache that comes with it? Sell it to the Trevlo Home Experts!</li>
        <li>Bad Mortgage - Selling your home is a great way to get out of your current mortgage quick.</li>
      </ul>
    </div>
  </div>
</section>

<section class="benefits">
  <h2 class="hd"><span class="blue">REASONS PEOPLE</span> <span class="green">WORK WITH TREVLO</span></h2>
  <div class="kicker">BENEFITS OF WORKING WITH US OVER A REALTOR</div>
  <div class="benefit" style="left:111px">
    <div class="badge" style="background:var(--green)"><svg width="60" height="60" viewBox="0 0 60 60" fill="none" stroke="#fff" stroke-width="3"><circle cx="30" cy="30" r="22"/><path d="M30 16v14l10 6"/></svg></div>
    <h3 class="green">QUICK TURNAROUND</h3><p>Sed ut perspiciatis unde omnis iste natus error sit voluptatem</p>
  </div>
  <div class="benefit" style="left:357px">
    <div class="badge" style="background:var(--blue)"><svg width="60" height="60" viewBox="0 0 60 60" fill="none" stroke="#fff" stroke-width="3"><path d="M14 14h18l16 16-18 18-16-16z"/><circle cx="22" cy="22" r="3"/></svg></div>
    <h3 class="blue">ZERO FEES</h3><p>Sed ut perspiciatis unde omnis iste natus error sit voluptatem</p>
  </div>
  <div class="benefit" style="left:604px">
    <div class="badge" style="background:var(--green)"><svg width="70" height="50" viewBox="0 0 70 50" fill="none" stroke="#fff" stroke-width="3"><rect x="4" y="8" width="40" height="28"/><path d="M44 16h12l10 10v10H44z"/><circle cx="16" cy="40" r="5"/><circle cx="54" cy="40" r="5"/></svg></div>
    <h3 class="green">STRESS &amp; HASSLE FREE</h3><p>Sed ut perspiciatis unde omnis iste natus error sit voluptatem</p>
  </div>
  <div class="benefit" style="left:851px">
    <div class="badge" style="background:var(--blue)"><svg width="70" height="60" viewBox="0 0 70 60" fill="none" stroke="#fff" stroke-width="3"><circle cx="42" cy="30" r="18"/><path d="M4 22h16M8 30h14M4 38h16"/><text x="42" y="37" font-size="20" font-family="Montserrat" font-weight="700" fill="#fff" stroke="none" text-anchor="middle">$</text></svg></div>
    <h3 class="blue">COLD HARD CASH FAST</h3><p>Sed ut perspiciatis unde omnis iste natus error sit voluptatem</p>
  </div>
</section>

<section class="experts">
  <h2 class="hd">WE'RE THE EXPERTS YOU TURN TO IN A PINCH.</h2>
  <span class="btn">GET STARTED</span>
</section>

<section class="how">
  <h2 class="hd"><span class="blue">HOW IT</span> <span class="green">WORKS</span></h2>
  <svg class="how-arrows" width="1200" height="542" viewBox="0 0 1200 542" fill="none" stroke="#888" stroke-width="1.5" stroke-dasharray="5 4">
    <path d="M255 280l55 32m-8 0l8 0-3-8"/>
    <path d="M465 320l55-32m-8-2l8 2-2 8"/>
    <path d="M692 280l55 32m-8 0l8 0-3-8"/>
    <path d="M890 320l55-32m-8-2l8 2-2 8"/>
  </svg>
  <div class="step" style="left:184px;top:248px"><span class="step-num" style="top:-18px;background:var(--blue)">01</span>
    <svg width="60" height="48" viewBox="0 0 60 48" fill="none" stroke="var(--blue)" stroke-width="2.5"><rect x="4" y="8" width="44" height="32"/><path d="M4 8l22 18 22-18"/></svg></div>
  <div class="step-label" style="left:184px;top:338px">CALL OR EMAIL US</div>

  <div class="step" style="left:388px;top:380px"><span class="step-num" style="bottom:-18px;background:var(--green)">02</span>
    <svg width="56" height="50" viewBox="0 0 56 50" fill="none" stroke="var(--green)" stroke-width="2.5"><rect x="6" y="4" width="30" height="20" rx="3"/><path d="M14 24l-4 8 10-8"/><rect x="22" y="20" width="28" height="18" rx="3"/></svg></div>
  <div class="step-label" style="left:388px;top:264px">SPEAK TO<br>A TREVLO EXPERT</div>

  <div class="step" style="left:598px;top:248px"><span class="step-num" style="top:-18px;background:var(--green)">03</span>
    <svg width="52" height="50" viewBox="0 0 52 50" fill="none" stroke="var(--green)" stroke-width="2.5"><rect x="4" y="8" width="44" height="38"/><path d="M4 18h44M14 4v8M38 4v8M12 26h28M12 34h28M20 22v20M32 22v20"/></svg></div>
  <div class="step-label" style="left:598px;top:338px">SCHEDULE A QUICK<br>WALK-THROUGH</div>

  <div class="step" style="left:817px;top:380px"><span class="step-num" style="bottom:-18px;background:var(--green)">04</span>
    <svg width="56" height="44" viewBox="0 0 56 44" fill="none" stroke="var(--green)" stroke-width="2.5"><rect x="4" y="8" width="48" height="26"/><circle cx="28" cy="21" r="7"/></svg></div>
  <div class="step-label" style="left:817px;top:264px">RECEIVE A<br>CASH OFFER</div>

  <div class="step" style="left:1013px;top:248px"><span class="step-num" style="top:-18px;background:var(--green)">05</span>
    <svg width="50" height="50" viewBox="0 0 50 50" fill="none" stroke="var(--green)" stroke-width="2.5"><rect x="6" y="6" width="30" height="36" rx="3"/><path d="M38 44V24m-6 6l6-6 6 6"/></svg></div>
  <div class="step-label" style="left:1013px;top:338px">GET PAID</div>
</section>

<section class="close-fast">
  <h2 class="hd"><span class="blue">CLOSE AS</span> <span class="green">FAST AS 7 DAYS!</span></h2>
  <div class="video" role="img" aria-label="Video still of a large two-storey house with a paved driveway">
    <span class="play"><svg width="30" height="30" viewBox="0 0 30 30"><path d="M9 5l17 10-17 10z" fill="#fff"/></svg></span>
  </div>
</section>

<section class="reviews">
  <h2 class="hd">REVIEWS</h2>
  <h3>HEAR FROM SATISFIED SELLERS</h3>
  <blockquote>
    <span class="q" style="left:-6px;top:-10px">&ldquo;</span>
    Sed ut perspiciatis unde omnis iste natus error sit voluptatem accusantium doloremque laudantium, totam rem aperiam, eaque ipsa quae ab illo inventore veritatis et quasi architecto beatae vitae dicta sunt explicabo. Nemo enim ipsam voluptatem quia voluptas sit aspernatur natus error sit voluptatem aut odit aut fugit
    <span class="q" style="right:0;bottom:-24px">&rdquo;</span>
  </blockquote>
  <div class="author">- Dana Whitfield</div>
</section>

<section class="faq">
  <h2 class="hd blue">QUESTIONS?</h2>
  <h3 class="green">WE HAVE THE ANSWERS</h3>
  <div class="faq-item" style="left:263px"><div class="qc" style="background:var(--green)">Q</div><h4>HOW FAST DOES THIS WORK?</h4></div>
  <div class="faq-item" style="left:600px"><div class="qc" style="background:var(--blue)">Q</div><h4>HOW FAST DOES THIS WORK?</h4><p>Sed ut perspiciatis unde omnis iste natus error sit voluptatem accusantium dolorem que laudantium</p></div>
  <div class="faq-item" style="left:938px"><div class="qc" style="background:var(--green)">Q</div><h4>WHAT IF MY HOME IS NOT IN GOOD SHAPE?</h4></div>
  <span class="btn">MORE FAQS</span>
</section>

<section class="contact" role="img" aria-label="Dimmed evening photo of a house behind the contact form">
  <h2 class="hd">CONTACT US</h2>
  <h3>SPEAK WITH A TREVLO EXPERT TODAY</h3>
  <div class="field" style="left:338px;top:168px;width:254px">Full Name :</div>
  <div class="field" style="left:604px;top:168px;width:256px">Phone :</div>
  <div class="field" style="left:338px;top:219px;width:254px">Email :</div>
  <div class="field" style="left:604px;top:219px;width:256px">Street Address :</div>
  <div class="field" style="left:338px;top:269px;width:254px">City :</div>
  <div class="field" style="left:604px;top:269px;width:256px">State :</div>
  <div class="field" style="left:338px;top:322px;width:522px">Zip :</div>
  <span class="btn">Get a Cash Offer</span>
</section>

<footer class="site-footer">
  <div class="brand"><span class="mark"></span>Trevlo Home Buyers</div>
  <div class="foot-call">
    <span class="ring"><svg width="22" height="22" viewBox="0 0 24 24"><path d="M6.6 10.8a15 15 0 006.6 6.6l2.2-2.2c.3-.3.7-.4 1-.2 1.1.4 2.3.6 3.6.6.6 0 1 .4 1 1V20c0 .6-.4 1-1 1A17 17 0 013 4c0-.6.4-1 1-1h3.5c.6 0 1 .4 1 1 0 1.3.2 2.5.6 3.6.1.3 0 .7-.2 1z" fill="var(--green)"/></svg></span>
    <div><div class="lbl">Call Us :</div><div class="num">(555) 010-4477</div></div>
  </div>
  <div class="social"><h4>Social Links</h4><div class="row"><span></span><span></span><span></span></div></div>
  <div class="cert" role="img" aria-label="Accreditation badge"></div>
  <div class="copyright">&copy; Copyright-2019 Trevlo Home Buyers.All rights reserved.<a>Terms and Conditions</a> &nbsp;|&nbsp; <a>Privacy Policy</a></div>
  <div class="disclaimer"><b>Disclaimer :</b>Sed ut perspiciatis unde omnis iste natus error sit voluptatem accusantium doloremque laudantium, totam rem aperiam, eaque ipsa quae ab illo inventore veritatis et quasi architecto beatae vitae dicta sunt explicabo.</div>
</footer>

</body>
</html>
```